Law Office Business Card

We need a business card design to include the following information:
Name of Firm: Halvern Law Group, P.A.
Address: 2417 Osprey Ln, Ste 208, West Palm Beach, FL 33512
Phone: 561-390-7752
Fax: 561-390-7789
Website: http://www.bhalvernlaw.example

We Need a place for the Person's name and email address. Please start with the following:
Lorna K. Tibbett, Esq.
lorna@bhalvernlaw.example

Industry/Entity Type

Business

```html
<!DOCTYPE html>
<html lang="en">
<head>
<meta charset="utf-8">
<title>Halvern Law Group – Business Card</title>
<link rel="stylesheet" href="https://fonts.googleapis.com/css2?family=Cinzel:wght@400;600&family=Tinos&family=Open+Sans:wght@400&display=swap">
<style>
  :root {
    --backdrop: #222120;
    --card-front: #f3f2ef;
    --card-back: #5e4d43;
    --ink-brown: #6b5a4c;
    --ink-dark: #2f2b28;
    --rule: #8a847e;
    --band-light: #c9c0b6;
    --band-dark: #6e5d50;
    --back-ink: #c2b5a9;
  }
  html, body {
    margin: 0;
    padding: 0;
    width: 1200px;
    height: 840px;
    overflow: hidden;
    background: var(--backdrop);
  }
  .canvas {
    position: relative;
    width: 1200px;
    height: 840px;
  }
  .card {
    position: absolute;
    width: 459px;
    height: 262px;
    box-shadow: 0 6px 16px rgba(0,0,0,0.55);
    overflow: hidden;
  }
  .card--front { left: 452px; top: 121px; background: var(--card-front); }
  .card--back  { left: 318px; top: 442px; background: var(--card-back); }

  /* front: person */
  .person {
    position: absolute;
    left: 23px;
    top: 30px;
  }
  .person__name {
    margin: 0;
    font-family: "Cinzel", serif;
    font-weight: 600;
    font-size: 15px;
    letter-spacing: 0.3px;
    color: var(--ink-brown);
  }
  .person__email {
    margin: 4px 0 0;
    font-family: "Tinos", serif;
    font-size: 13.5px;
    color: var(--ink-dark);
  }

  /* front: firm mark */
  .firm-mark {
    position: absolute;
    right: 26px;
    top: 78px;
    display: flex;
    align-items: center;
    gap: 10px;
  }
  .firm-mark__square {
    width: 24px;
    height: 24px;
    border: 1.5px solid var(--ink-brown);
  }
  .firm-mark__name {
    font-family: "Cinzel", serif;
    font-weight: 400;
    font-size: 19px;
    line-height: 1.15;
    color: var(--ink-brown);
    text-align: center;
  }

  .firm-title {
    position: absolute;
    left: 23px;
    top: 153px;
    margin: 0;
    font-family: "Cinzel", serif;
    font-weight: 600;
    font-size: 17px;
    letter-spacing: 0.3px;
    color: var(--ink-brown);
  }
  .title-rule {
    position: absolute;
    left: 23px;
    right: 24px;
    top: 178px;
    height: 0;
    border-top: 1px solid var(--rule);
  }

  .contact-list {
    position: absolute;
    left: 24px;
    top: 186px;
    margin: 0;
    padding: 0;
    list-style: none;
    font-family: "Tinos", serif;
    font-size: 13.5px;
    color: var(--ink-dark);
  }
  .contact-list li {
    display: flex;
    align-items: center;
    gap: 6px;
    height: 17.5px;
  }
  .contact-list svg { width: 12px; height: 12px; fill: var(--ink-dark); }

  .address {
    position: absolute;
    right: 26px;
    top: 203px;
    margin: 0;
    font-family: "Tinos", serif;
    font-style: normal;
    font-size: 13.5px;
    line-height: 17.5px;
    text-align: right;
    color: var(--ink-dark);
  }

  .footer-band {
    position: absolute;
    left: 0;
    right: 0;
    bottom: 0;
    height: 12px;
    border-top: 2px solid var(--band-light);
    background: linear-gradient(180deg, #a39384 0%, var(--band-dark) 100%);
  }

  /* back */
  .back-mark {
    position: absolute;
    right: 50px;
    top: 160px;
    display: flex;
    align-items: center;
    gap: 8px;
  }
  .back-mark__square {
    width: 18px;
    height: 18px;
    border: 1.5px solid var(--back-ink);
  }
  .back-mark__name {
    font-family: "Cinzel", serif;
    font-weight: 400;
    font-size: 15px;
    line-height: 1.15;
    color: var(--back-ink);
    text-align: center;
  }
  .back-web {
    position: absolute;
    right: 24px;
    top: 226px;
    font-family: "Open Sans", sans-serif;
    font-size: 11.5px;
    letter-spacing: 1.2px;
    color: var(--back-ink);
  }
</style>
</head>
<body>
<main class="canvas">

  <section class="card card--front" aria-label="Card front">
    <div class="person">
      <p class="person__name">Lorna K. Tibbett, Esq.</p>
      <p class="person__email">lorna@bhalvernlaw.example</p>
    </div>

    <div class="firm-mark">
      <span class="firm-mark__square"></span>
      <span class="firm-mark__name">Halvern Law<br>Group</span>
    </div>

    <h1 class="firm-title">Halvern Law Group, P.A.</h1>
    <div class="title-rule"></div>

    <ul class="contact-list">
      <li>
        <svg viewBox="0 0 24 24" aria-hidden="true"><path d="M6.6 10.8a15.1 15.1 0 0 0 6.6 6.6l2.2-2.2a1 1 0 0 1 1-.25 11.4 11.4 0 0 0 3.6.57 1 1 0 0 1 1 1V20a1 1 0 0 1-1 1A17 17 0 0 1 3 4a1 1 0 0 1 1-1h3.5a1 1 0 0 1 1 1c0 1.25.2 2.45.57 3.57a1 1 0 0 1-.25 1z"/></svg>
        561-390-7752
      </li>
      <li>
        <svg viewBox="0 0 24 24" aria-hidden="true"><path d="M6 2h12v6H6zM3 9h18a2 2 0 0 1 2 2v7h-4v4H5v-4H1v-7a2 2 0 0 1 2-2zm4 8v3h10v-3z"/></svg>
        561-390-7789
      </li>
      <li>
        <svg viewBox="0 0 24 24" aria-hidden="true"><circle cx="12" cy="12" r="10"/><path d="M8 6c2 1 1 3 3 4s1 3 3 3" stroke="#f3f2ef" stroke-width="2" fill="none"/></svg>
        www.bhalvernlaw.example
      </li>
    </ul>

    <address class="address">
      2417 Osprey Ln, Ste 208<br>
      West Palm Beach, FL 33512
    </address>

    <div class="footer-band"></div>
  </section>

  <section class="card card--back" aria-label="Card back">
    <div class="back-mark">
      <span class="back-mark__square"></span>
      <span class="back-mark__name">Halvern Law<br>Group</span>
    </div>
    <div class="back-web">www.bhalvernlaw.example</div>
  </section>

</main>
</body>
</html>
```